Website R86 coffee

I am opening a small business selling locally roasted coffee online. To start with I want a site with three pages. 1. A welcome page with logo and mission/vision. 2. Shopping/ordering page. 3. About Us page. The brand is "R86 Coffee - A warm start to every day". We are giving back to the downs syndrome community by employing people with down syndrome (Trisomy 21) and buy donating to down syndrome research.

Target Market(s)

Families and friends of people with downs syndrome

Coding

Coded - Design and coding required

Number of Pages Required

3 page

```html
<!DOCTYPE html>
<html lang="en">
<head>
<meta charset="utf-8">
<title>R86 Coffee - A warm start to every day</title>
<link href="https://fonts.googleapis.com/css2?family=Roboto:wght@300;400;500;700&display=swap" rel="stylesheet">
<style>
:root{
  --brown-bar:#6a3f26;
  --brown-dark:#4a2418;
  --brown-mid:#6b4029;
  --ink:#111;
  --text:#333;
  --muted:#555;
  --cream:#fdf6ef;
  --footer:#eeeeec;
  --gold:#e7a615;
  --white:#fff;
}
*{box-sizing:border-box;margin:0;padding:0}
html,body{width:1200px;height:3679px;overflow:hidden}
body{position:relative;font-family:'Roboto',sans-serif;color:var(--text);background:var(--white)}
.abs{position:absolute}
a{color:inherit;text-decoration:none}

.promo-bar{left:0;top:0;width:1200px;height:33px;background:var(--brown-bar);color:var(--white);font-size:13px;display:flex;align-items:center;justify-content:center;gap:4px}
.promo-bar b{font-size:15px}
.promo-bar u{margin-left:4px}

.hero-photo{left:0;top:33px;width:1200px;height:667px;background:linear-gradient(180deg,#e9eee0 0%,#a9be7a 18%,#6f8f3c 42%,#566f2b 55%,#7a5330 62%,#5a3520 80%,#3c2416 100%)}
.brand{left:100px;top:40px;width:179px;height:50px;display:flex;align-items:center;gap:10px;font-size:26px;font-weight:400;color:var(--ink);letter-spacing:1px}
.brand .mark{width:14px;height:14px;background:var(--ink)}
.main-nav{left:467px;top:52px;display:flex;gap:0;font-size:15px;color:var(--ink);font-weight:500}
.main-nav span{position:absolute;white-space:nowrap;display:flex;align-items:center;gap:5px;font-weight:400}
.main-nav svg{width:18px;height:18px}
.hero-title{left:119px;top:262px;font-size:78px;font-weight:300;color:var(--white);letter-spacing:1px}
.hero-title b{font-weight:700}
.hero-sub{left:119px;top:350px;font-size:36px;color:var(--white);font-weight:400}
.btn-dark{background:var(--ink);color:var(--white);font-size:15px;font-weight:500;display:flex;align-items:center;justify-content:center;text-transform:uppercase}
.hero-btn{left:119px;top:421px;width:147px;height:40px}
.slide-arrow{top:380px;width:20px;height:40px}

.purpose-card{top:633px;width:472px;height:201px;color:var(--white);border-radius:3px}
.purpose-card.vision{left:114px;background:var(--brown-dark)}
.purpose-card.mission{left:614px;background:var(--brown-mid)}
.purpose-icon{left:27px;top:36px;width:76px;height:76px;border-radius:50%;background:var(--white)}
.purpose-icon svg{width:76px;height:76px}
.purpose-card h2{position:absolute;left:110px;top:42px;font-size:27px;font-weight:400}
.purpose-card h2 b{font-weight:500}
.purpose-card p{position:absolute;left:110px;top:84px;width:340px;font-size:15px;line-height:30px;font-weight:300}

.about-photo{left:99px;top:927px;width:597px;height:432px;background:linear-gradient(120deg,#7d7468 0%,#4b4a3f 35%,#2f2a24 70%,#1d1b19 100%)}
.about-accent{left:830px;top:1133px;width:256px;height:194px;border-right:6px solid var(--brown-dark);border-bottom:6px solid var(--brown-dark)}
.about-card{left:607px;top:969px;width:474px;height:348px;background:var(--white);box-shadow:0 2px 14px rgba(0,0,0,.08);padding:30px 24px}
.section-title{font-size:34px;color:var(--ink);font-weight:300;text-transform:uppercase}
.section-title b{font-weight:500}
.rule{width:80px;height:4px;background:var(--ink);margin-top:10px}
.about-card p{margin-top:22px;font-size:14.5px;line-height:25px;color:var(--muted)}
.btn-line{margin-top:18px;width:154px;height:43px;border:2px solid var(--ink);font-size:15px;display:flex;align-items:center;justify-content:center;color:var(--ink);text-transform:uppercase}

.sellers-band{left:0;top:1454px;width:1200px;height:440px;background:radial-gradient(circle at 80% 30%,#6a4028 0%,#3b2216 45%,#1e120c 100%)}
.sellers-title{left:0;top:1638px;width:1200px;text-align:center;color:var(--white);font-size:37px;font-weight:300}
.sellers-title b{font-weight:500}
.cream{left:0;top:1894px;width:1200px;height:732px;background:var(--cream)}
.product{top:1731px;width:240px;height:318px;background:var(--white);box-shadow:0 1px 6px rgba(0,0,0,.1);text-align:center}
.product .shot{margin:6px;height:187px;background:radial-gradient(ellipse at 50% 50%,#5a3522 0%,#4a2a1a 30%,#ececec 58%,#f3f3f3 100%)}
.product .level{margin-top:8px;font-size:11px;color:var(--muted);text-transform:uppercase}
.product .name{margin-top:6px;font-size:15.5px;font-weight:500;color:var(--ink)}
.product .price{margin-top:8px;font-size:14px;color:var(--text)}
.product .rating{margin-top:8px;font-size:10px;color:#777}
.product .rating span{color:var(--gold);letter-spacing:1px}

.reviews-stars{left:0;top:2118px;width:1200px;text-align:center;font-size:30px;color:var(--ink);letter-spacing:2px}
.reviews-title{left:0;top:2158px;width:1200px;text-align:center;font-size:31px;color:var(--ink);font-weight:400;text-transform:uppercase}
.reviews-title b{font-weight:500}
.review{top:2218px;width:476px;height:325px;background:var(--white);border-radius:10px;padding:36px 30px}
.review .quote{font-size:80px;line-height:60px;font-weight:700;color:var(--ink);font-family:'Roboto',serif;height:38px}
.review h3{margin-top:16px;font-size:13.5px;font-weight:500;color:var(--ink)}
.review p{margin-top:8px;font-size:15.5px;line-height:25.7px;color:var(--text)}
.review .author{margin-top:12px;display:flex;align-items:center;gap:14px}
.review .avatar{width:50px;height:50px;border-radius:50%;background:linear-gradient(135deg,#8a94a0,#4d5864)}
.review .who{font-size:13.5px;font-weight:700;color:var(--ink)}
.review .who span{display:block;color:var(--gold);font-size:10px;letter-spacing:1px;font-weight:400}

.quote-photo{left:497px;top:2719px;width:596px;height:432px;background:linear-gradient(90deg,#2c241d 0%,#5c4431 30%,#c9932e 60%,#8a6a48 85%,#3a2c22 100%)}
.quote-accent{left:106px;top:2924px;width:255px;height:195px;border-left:6px solid var(--brown-mid);border-bottom:6px solid var(--brown-mid)}
.quote-card{left:111px;top:2760px;width:475px;height:350px;background:var(--white);box-shadow:0 2px 14px rgba(0,0,0,.08);padding:32px 26px}
.field{margin-top:18px;width:422px;height:46px;border:1px solid #ccc;font-size:15px;color:var(--muted);padding:0 14px;display:flex;align-items:center}
.field + .field{margin-top:8px}
.quote-card .btn-dark{margin-top:14px;width:174px;height:46px;font-size:16px}

.site-footer{left:0;top:3246px;width:1200px;height:433px;background:var(--footer)}
.beans-strip{left:0;top:3571px;width:1200px;height:108px;background:linear-gradient(180deg,rgba(238,238,236,0) 0%,#6b4a36 40%,#3a2619 100%)}
.footer-brand{left:100px;top:3326px;width:154px;height:151px;display:flex;align-items:center;justify-content:center;gap:8px;font-size:26px;color:var(--ink);font-weight:400}
.footer-brand .mark{width:14px;height:14px;background:var(--ink)}
.footer-col{top:3322px}
.footer-col h4{font-size:17px;font-weight:500;color:var(--ink);margin-bottom:10px}
.footer-col li{list-style:none;font-size:14px;color:var(--text);line-height:28.5px}
.social{top:3358px;display:flex;gap:7px;left:983px}
.social i{width:35px;height:35px;border-radius:50%;background:var(--white);display:block}
.footer-rule{left:100px;top:3516px;width:1002px;height:1px;background:#b9b9b9}
.copyright{left:100px;top:3535px;font-size:13px;color:var(--text)}
.pay{top:3534px;left:759px;display:flex;gap:7px}
.pay i{display:block;width:32px;height:20px;border-radius:2px;background:#c8c8d4}
</style>
</head>
<body>

<div class="abs promo-bar"><b>Save 5%</b> With Subscription Orders <u>Learn more</u></div>

<div class="abs hero-photo" role="img" aria-label="Green coffee plantation hills with a white cup of coffee, coffee cherries and roasted beans on a wooden table"></div>

<div class="abs brand"><span class="mark"></span>R86 Coffee</div>

<nav class="abs main-nav">
  <span style="left:0">Home</span>
  <span style="left:92px">Shopping</span>
  <span style="left:209px">About Us</span>
  <span style="left:317px"><svg viewBox="0 0 24 24" fill="none" stroke="#111" stroke-width="1.6"><path d="M4 14v-2a8 8 0 0116 0v2"/><rect x="3" y="13" width="4" height="6" rx="1"/><rect x="17" y="13" width="4" height="6" rx="1"/></svg>Help &#709;</span>
  <span style="left:410px"><svg viewBox="0 0 24 24" fill="none" stroke="#111" stroke-width="1.6"><circle cx="12" cy="8" r="4"/><path d="M4 21c1-5 5-7 8-7s7 2 8 7"/></svg>My Account</span>
  <span style="left:538px"><svg viewBox="0 0 24 24" fill="none" stroke="#111" stroke-width="1.6"><path d="M2 4h3l3 11h11l2-8H6"/><circle cx="9" cy="19" r="1.5"/><circle cx="18" cy="19" r="1.5"/></svg>My Cart &#709;</span>
</nav>

<h1 class="abs hero-title"><b>R86</b> COFFEE</h1>
<div class="abs hero-sub">A warm start to every day</div>
<a class="abs btn-dark hero-btn">Shop Now</a>
<svg class="abs slide-arrow" style="left:62px" viewBox="0 0 20 40" fill="none" stroke="#fff" stroke-width="1.5"><path d="M16 4L4 20l12 16"/></svg>
<svg class="abs slide-arrow" style="left:1118px" viewBox="0 0 20 40" fill="none" stroke="#fff" stroke-width="1.5"><path d="M4 4l12 16L4 36"/></svg>

<section class="abs purpose-card vision">
  <div class="abs purpose-icon"><svg viewBox="0 0 76 76" fill="none" stroke="#111" stroke-width="2.4"><path d="M16 38c6-8 14-12 22-12s16 4 22 12c-6 8-14 12-22 12s-16-4-22-12z"/><circle cx="38" cy="38" r="7"/><circle cx="38" cy="38" r="2.5" fill="#111"/></svg></div>
  <h2><b>OUR</b> VISION</h2>
  <p>Develop A Company That Markets Coffee And Related Products To Family And Friends Of The Down Syndrome Community</p>
</section>
<section class="abs purpose-card mission">
  <div class="abs purpose-icon"><svg viewBox="0 0 76 76" fill="none" stroke="#111" stroke-width="2.2"><circle cx="37" cy="40" r="20"/><circle cx="37" cy="40" r="13"/><circle cx="37" cy="40" r="6"/><path d="M37 40l18-18M50 20v7h7"/></svg></div>
  <h2><b>OUR</b> MISSION</h2>
  <p>Create And Grow An Online Company Selling Contract Roasted Coffee. As Growth Permits Become A Fully Vertically Integrated ...</p>
</section>

<div class="abs about-photo" role="img" aria-label="Roaster checking freshly roasted beans beside a coffee roasting machine"></div>
<div class="abs about-accent"></div>
<section class="abs about-card">
  <h2 class="section-title"><b>About</b> R86 Coffee</h2>
  <div class="rule"></div>
  <p>Lorem ipsum dolor sit amet, consur adipiscind do eiusmod tempor incididunt ut labore et dna aliqua. Quis ipsum suspendisse ultrices gravida. Risus commodo viverracenas accumsan lus vel facilisis. Lorem ipsum dolor sit amet, consur adipcing elit, sed do eiusmod tempor incididunt ut labore et dna aliqua. Quis ipsum suspendisse ultrices gravida. Risus commodo</p>
  <a class="btn-line">Learn More</a>
</section>

<div class="abs sellers-band" role="img" aria-label="Close-up of dark roasted coffee beans"></div>
<div class="abs cream"></div>
<h2 class="abs sellers-title"><b>BEST</b> SELLERS</h2>

<article class="abs product" style="left:99px"><div class="shot" role="img" aria-label="Pile of light roast coffee beans"></div><div class="level">Light Roast Lervel</div><div class="name">Autumn Roaster's Blend</div><div class="price">$10.55 - $19.75/lb</div><div class="rating"><span>★★★★★</span> (24 reviews)</div></article>
<article class="abs product" style="left:353px"><div class="shot" role="img" aria-label="Pile of medium roast coffee beans"></div><div class="level">Medium Roast Lervel</div><div class="name">Autumn Roaster's Blend</div><div class="price">$10.55 - $19.75/lb</div><div class="rating"><span>★★★★★</span> (24 reviews)</div></article>
<article class="abs product" style="left:607px"><div class="shot" role="img" aria-label="Pile of medium dark roast coffee beans"></div><div class="level">Medium Dark Roast Lervel</div><div class="name">Autumn Roaster's Blend</div><div class="price">$10.55 - $19.75/lb</div><div class="rating"><span>★★★★★</span> (24 reviews)</div></article>
<article class="abs product" style="left:860px"><div class="shot" role="img" aria-label="Pile of dark roast coffee beans"></div><div class="level">Dark Roast Lervel</div><div class="name">Autumn Roaster's Blend</div><div class="price">$10.55 - $19.75/lb</div><div class="rating"><span>★★★★★</span> (24 reviews)</div></article>

<div class="abs reviews-stars">★★★★★</div>
<h2 class="abs reviews-title"><b>Real Customers</b> About Us</h2>

<article class="abs review" style="left:110px">
  <div class="quote">&#8220;</div>
  <h3>WONDERFUL BUSINESS</h3>
  <p>Lorem ipsum dolor sit amet, cetur adipiscit, sed do eiusmod tempor ididunt ut labore et dolore magna. is m suspendisse ultrices gravida. Risus codo viverra maecenaccumsan lacus vel facilisis. Lorem ipsum dolor sit amet, cetur adipiscing elit, sed do eiusmod tempor ididunt ut</p>
  <div class="author"><div class="avatar" role="img" aria-label="Customer portrait"></div><div class="who">- Sam Carter<span>★★★★★</span></div></div>
</article>
<article class="abs review" style="left:613px">
  <div class="quote">&#8220;</div>
  <h3>WONDERFUL BUSINESS</h3>
  <p>Lorem ipsum dolor sit amet, cetur adipiscit, sed do eiusmod tempor ididunt ut labore et dolore magna. is m suspendisse ultrices gravida. Risus codo viverra maecenaccumsan lacus vel facilisis. Lorem ipsum dolor sit amet, cetur adipiscing elit, sed do eiusmod tempor ididunt ut</p>
  <div class="author"><div class="avatar" role="img" aria-label="Customer portrait"></div><div class="who">- Sam Carter<span>★★★★★</span></div></div>
</article>

<div class="abs quote-photo" role="img" aria-label="Woman in a yellow sweater holding a cup of coffee in a cafe"></div>
<div class="abs quote-accent"></div>
<section class="abs quote-card">
  <h2 class="section-title"><b>Get A</b> Free Quote</h2>
  <div class="rule"></div>
  <div class="field">Your Name*</div>
  <div class="field">E-Mail*</div>
  <div class="field">Phone*</div>
  <a class="btn-dark">Submit Message</a>
</section>

<footer class="abs site-footer"></footer>
<div class="abs beans-strip" role="img" aria-label="Roasted coffee beans with green coffee leaves"></div>
<div class="abs footer-brand"><span class="mark"></span>R86 Coffee</div>

<div class="abs footer-col" style="left:354px"><h4>QUICK LINKS</h4><ul><li>Home</li><li>Shopping</li><li>About Us</li><li>Contact</li></ul></div>
<div class="abs footer-col" style="left:556px"><h4>HELP &amp; FAQ</h4><ul><li>FAQs</li><li>Returns</li><li>Contact Us</li><li>Chek Order Status</li><li>Accessibility</li></ul></div>
<div class="abs footer-col" style="left:766px"><h4>COMPANY</h4><ul><li>Careers</li><li>Affiliates</li><li>Terms &amp; Conditions</li><li>Privacy</li><li>Privacy Rights</li></ul></div>
<div class="abs footer-col" style="left:981px"><h4>CONNECT</h4></div>
<div class="abs social"><i></i><i></i><i></i></div>

<div class="abs footer-rule"></div>
<div class="abs copyright">©Copyright ©2021 R86 coffee. All Rights Reserved.</div>
<div class="abs pay"><i></i><i></i><i></i><i></i><i></i><i></i><i></i><i></i><i></i></div>

</body>
</html>
```